Thank you for exploring whether you are interested in creating a book cover for The Insight Lantern!

The cover should look professional yet appeal to a person who is open to approaching life more deeply.

The logo that I've uploaded is something that you are welcome to use in your book cover design but is not required to be the primary graphic.

The following is a description of The Insight Lantern and its purpose.
RADICAL CLARITY IS POSSIBLE

Are you tired of hitting up against your limitations? Do you wish you could be more effective in everything you do? What would it be like if you could walk confidently into any situation and automatically comprehend it, organize your thoughts, and respond creatively? This kind of radical clarity is not only possible, it’s right in front of you—and The Insight Lantern: Notice Every Signal. Hold Bold Dialogues. Build the Path You Choose. shows you the pathway to get there!

In the book, Dr. Gavin Terlecki draws on over 30 years of experience with executive coaching and leadership development to deliver priceless wisdom about how to see clearly in today’s complex and uncertain world. Using his Insight Lantern, you’ll discover where you’re stuck and why, find your authentic direction, and learn to engage creatively with life so you can start getting what you really want.

A TRANSFORMATIONAL TOOL

The Insight Lantern is a cutting-edge leadership development tool that supports you to activate your maximum potential, both personally and professionally. It’s based on the idea that there are four fundamental building blocks to reality: Intentions, Actions, Facts, and Stories. Understanding the differences between these dimensions of your experience and learning how they work together is the key to forging a clear path toward your destination in life. The Insight Lantern organizes these four main building blocks around the two polarities of a compass:

1. North to South – Intentions to Actions
We all have billions of intentions, but how many do we actually put into action? In this polarity you learn to notice and implement your intentions in order to generate more effective actions and create meaningful outcomes in your life.

2. East vs. West – Facts vs. Stories
We all create stories to make sense of life, but how many of us actually get clear on the facts to see where our stories might be off? In this polarity you learn to discern the objective facts from your subjective interpretations and stories, illuminating a clearer perspective to uncover what’s been blocking you on the path to success.

Using The Insight Lantern you’ll discover how naming and implementing your intentions in life naturally results in more effective behavior and actions, and how distinguishing the real facts from your interpretations of any situation can propel you toward radical clarity and true fulfillment.

BOLD DIALOGUES

The key benefit of using The Insight Lantern is that you’ll have more of what Gavin calls “Bold Dialogues.” Bold Dialogues are those that move you closer to what you’re wanting in life—the kind of human-to-human interactions that actually make a difference. By applying The Insight Lantern, you gain critical insight that opens your eyes to new opportunities for Bold Dialogues, helping you draw on your imagination and move beyond your current stance toward a positive outcome. Every conversation is a possibility waiting to be discovered. The more Bold Dialogues you have, the more profound and meaningful shifts you activate in your life.

PRACTICAL GUIDANCE

The book doesn’t just give you a theoretical understanding of how to gain more clarity in your life. Dr. Terlecki provides you with clear, practical steps to develop the core competencies you need to start getting the results you want. As you explore the book, you’ll find:

• A thorough description of all the directions of The Insight Lantern, each with three main points to focus your energy on.
• Case studies from Gavin’s many clients who have successfully used The Insight Lantern to transform their own lives.
• Hands-on practices Gavin has developed to help you put your new skills to use immediately.
• Step-by-step guidance to apply The Insight Lantern in any situation, including real-life stories from people who have experienced genuine transformation using this tool.

The Insight Lantern will help you to deepen your understanding of the challenges in your life, integrate new competencies to boost your effectiveness, and awaken to exciting opportunities for your own growth, leadership, and success!

ABOUT THE AUTHOR

Dr. Gavin Terlecki has over 30 years of experience with leadership development and executive coaching work. As owner and principal coach of Terlecki Growth Advisors, he has been integrating the fields of management consulting, business psychology, and leadership coaching since 1983. Gavin holds a Ph.D. in psychodynamic and group psychology from the Halvern Graduate Academy, an M.A. in human growth and potential from the Marlowe Ridge University, and a B.A. in accounting and Business Administration from Denby Valley University. He is the creator of The Insight Lantern™, a leadership development tool that supports people to see life clearly, wake up to exciting opportunities for their own growth and leadership, and take empowered action toward true success. Gavin’s combination of business expertise, human compassion, and incisive questions help his clients achieve unprecedented results.

Target Market(s)

Out intended audience is folks who would like to be more effective and to grow and transform. This being more productive and developing could be in their careers or their personal lives.

Industry/Entity Type

It Professional

Requirements
Must have
• Stock images, if used, that I can purchase exclusively or that you can easily create specifically for the book once you are the chosen designer. I completely understand using stock imaging in your submissions pre-selection.
Nice to have
• Ideally the cover will include both the title and subtitle.

```html
<!DOCTYPE html>
<html lang="en">
<head>
<meta charset="utf-8">
<title>The Insight Lantern — Book Cover</title>
<link href="https://fonts.googleapis.com/css2?family=Archivo+Black&family=Inter:wght@200;700&family=Montserrat:wght@700&display=swap" rel="stylesheet">
<style>
  :root {
    --canvas-bg: #e4e4e4;
    --cover-dark: #3b3b3b;
    --band-grey: #5c5c5c;
    --title-black: #0d0d0d;
    --accent-orange: #e08119;
    --author-grey: #2e2e2e;
    --forest-mid: #7a7a7a;
    --forest-light: #cfcfcf;
  }
  * { margin: 0; padding: 0; box-sizing: border-box; }
  html, body { width: 1200px; height: 1000px; overflow: hidden; }
  body {
    background: var(--canvas-bg);
    display: flex;
    align-items: center;
    justify-content: center;
  }
  .book-cover {
    position: relative;
    width: 600px;
    height: 820px;
    background: var(--cover-dark);
    overflow: hidden;
  }
  .cover-photo {
    position: absolute;
    left: 0; top: 255px;
    width: 600px; height: 345px;
    background:
      linear-gradient(90deg, rgba(30,30,30,.55) 0%, rgba(0,0,0,0) 35%, rgba(0,0,0,0) 70%, rgba(30,30,30,.45) 100%),
      linear-gradient(180deg, var(--forest-mid) 0%, var(--forest-light) 60%, var(--forest-mid) 100%);
  }
  .accent-line {
    position: absolute;
    left: 0; top: 255px;
    width: 600px; height: 345px;
  }
  .lower-band {
    position: absolute;
    left: 0; top: 600px;
    width: 600px; height: 220px;
    background: var(--band-grey);
  }
  .title-block {
    position: absolute;
    left: 14px; top: 96px;
    color: var(--title-black);
  }
  .title-article {
    font-family: 'Inter', sans-serif;
    font-weight: 200;
    font-size: 40px;
    letter-spacing: -2px;
    line-height: 1;
  }
  .title-main {
    font-family: 'Archivo Black', sans-serif;
    font-size: 62px;
    letter-spacing: -3px;
    line-height: .9;
    margin-top: -6px;
    white-space: nowrap;
  }
  .subtitle {
    position: absolute;
    left: 0; top: 222px;
    width: 600px;
    text-align: center;
    font-family: 'Montserrat', sans-serif;
    font-weight: 700;
    font-size: 18px;
    letter-spacing: .55em;
    color: var(--accent-orange);
  }
  .author {
    position: absolute;
    left: 0; top: 660px;
    width: 600px;
    text-align: center;
    font-family: 'Inter', sans-serif;
    font-weight: 700;
    font-size: 24px;
    letter-spacing: -1px;
    color: var(--author-grey);
  }
</style>
</head>
<body>
  <main class="book-cover">
    <div class="cover-photo" role="img" aria-label="Black and white photograph of tall pine trunks in a sunlit forest"></div>
    <svg class="accent-line" viewBox="0 0 600 345" aria-hidden="true">
      <g fill="var(--accent-orange)">
        <rect x="0" y="290" width="60" height="22"/>
        <polygon points="170,235 330,195 334,205 174,251"/>
        <polygon points="400,173 540,125 541,131 402,181"/>
      </g>
    </svg>
    <div class="lower-band"></div>
    <h1 class="title-block">
      <span class="title-article">The</span><br>
      <span class="title-main">Insight Lantern</span>
    </h1>
    <p class="subtitle">NOTICE EVERY SIGNAL</p>
    <p class="author">Dr. Gavin Terlecki</p>
  </main>
</body>
</html>
```